Marijuana Lifestyle Multi-Shop Brand Website

We need a website that provides an online retail shop for our products, along with the additional functionality:

Main Page: Slider with great photography (we are still looking for a professional photographer to take photos for us.

Shop Tab: E-commerce site.
- Main Categories:
- Accessories
- Bubblers
- Dry Pieces
- Scientific Glass
- Water Pipes
- Custom Shop
- University Store

Stores/Resellers: This is a store look-up, so people can enter their zipcode and find our resellers and partners.

Brand Partners: Just a basic filter and page so that we can highlight our partners and why we've selected them.

Contact Us: Basic Form
- Career Page: Basic Page

About Us: Basic Page

Blog:

Search Bar:

Essentially, we want a near exact copy of this website, but with our brand, logo and content. https://plumcratevault.com/

This site is really really simple, but we like simple.

Our reserved domain address is: www.runsowmend.com

About Us:
We are multi-shop for marijuana-related accessories. We sell quality glass pipes, vaporizers, amazing storage options, dime bags, custom t-shirts and other stuff.

We have a network of resellers that allow us to put in micro-installations into gift shops, convenience stores, tobacco stores, etc. and we are trying to change the overall perception that buying these items should be mainstream and as transparent as going to the Elk or the Birch Depot.

I've attached a logo that should give you an idea of our color scheme. We don't have our photography yet for the slider

As an FYI, for the e-commerce part of my website, I already have a license for WP SwiftTill.

```html
<!DOCTYPE html>
<html lang="en">
<head>
<meta charset="utf-8">
<title>Verdant Twin – Water Pipes</title>
<link rel="stylesheet" href="https://fonts.googleapis.com/css2?family=Rosario:wght@400;600&display=swap">
<style>
  :root {
    --ink: #111111;
    --olive: #3b4418;
    --rule: #4a5022;
    --frame: #9a9a9a;
    --paper: #ffffff;
    --btn-text: #f2f2e8;
    --social-1: #1d5fa8;
    --social-2: #1aa3d6;
    --social-3: #7a3a9a;
    --social-4: #c8281e;
  }
  * { box-sizing: border-box; margin: 0; padding: 0; }
  html, body { width: 960px; height: 1200px; overflow: hidden; background: var(--paper); }
  body { position: relative; font-family: "Rosario", sans-serif; color: var(--ink); font-variant-numeric: lining-nums; }

  .site-header { position: absolute; inset: 0 0 auto 0; height: 160px; }
  .nav-link { position: absolute; top: 70px; font-size: 20px; color: var(--ink); text-decoration: none; }
  .nav-rule { position: absolute; top: 103px; height: 2px; background: var(--rule); }
  .search-field {
    position: absolute; left: 800px; top: 23px; width: 137px; height: 18px;
    border: 2px solid var(--olive); border-radius: 9px;
    font-size: 11px; font-style: italic; color: #999; padding: 0 8px; line-height: 14px;
  }
  .brand-badge {
    position: absolute; left: 407px; top: 15px; width: 140px; height: 140px; border-radius: 50%;
    background: var(--paper); box-shadow: 0 3px 6px rgba(0,0,0,.25);
    display: flex; align-items: center; justify-content: center;
  }
  .brand-badge span {
    width: 126px; height: 126px; border-radius: 50%; background: var(--olive);
    display: flex; align-items: center; justify-content: center; text-align: center;
    color: var(--paper); font-size: 21px; font-weight: 600; line-height: 1.05;
  }

  .page-title { position: absolute; left: 157px; top: 143px; font-size: 31px; font-weight: 400; }

  .product { position: absolute; width: 225px; }
  .product-photo { width: 225px; height: 225px; border: 1px solid var(--frame); }
  .photo-clear-trio   { background: linear-gradient(90deg, #fff 8%, #c9cbe6 28%, #eddcec 50%, #c3c6e8 72%, #fff 92%); }
  .photo-acrylic      { background: linear-gradient(90deg, #fff 10%, #8fc8e8 30%, #8fd39a 50%, #f0907a 70%, #fff 90%); }
  .photo-amber-tall   { background: linear-gradient(90deg, #fff 25%, #f3c98a 50%, #fff 75%); }
  .photo-clear-beaker { background: linear-gradient(90deg, #fff 25%, #d9dcd9 50%, #fff 75%); }
  .photo-bubbler-row  { background: linear-gradient(90deg, #fff 5%, #c8a8d0 25%, #9fd3cf 45%, #b7a0d8 65%, #d8a3b8 85%, #fff 97%); }
  .photo-navy-amber   { background: linear-gradient(180deg, #fff 5%, #6d7aa8 25%, #e8ecef 50%, #f1dfa8 80%, #fff 97%); }
  .photo-striped      { background: linear-gradient(135deg, #fff 15%, #f1e6a0 40%, #e9a08a 55%, #f3eab0 70%, #fff 88%); }
  .photo-assorted     { background: linear-gradient(90deg, #fff 5%, #e8dca4 20%, #dfe6e6 45%, #f0b69a 70%, #f1c98e 85%, #fff 97%); }
  .photo-slim-green   { background: linear-gradient(90deg, #fff 30%, #b9e0be 50%, #fff 70%); }

  .product-name { position: absolute; left: 2px; top: 232px; font-size: 14px; white-space: nowrap; }
  .product-price { position: absolute; left: 2px; top: 249px; font-size: 13px; }
  .add-to-cart {
    position: absolute; left: 133px; top: 234px; width: 93px; height: 27px;
    background: var(--olive); color: var(--btn-text); border: none;
    box-shadow: 2px 2px 3px rgba(0,0,0,.3);
    font-family: inherit; font-size: 12.5px; letter-spacing: .3px; white-space: nowrap;
  }

  .site-footer { position: absolute; left: 58px; top: 1131px; width: 844px; border-top: 1px solid #333; }
  .social { position: absolute; top: 1149px; width: 32px; height: 32px; border-radius: 50%;
    color: var(--paper); font-size: 8px; font-weight: 600; display: flex; align-items: center; justify-content: center; }
</style>
</head>
<body>
  <header class="site-header">
    <a class="nav-link" style="left:92px">Shop</a>
    <a class="nav-link" style="left:159px">Store Locator</a>
    <a class="nav-link" style="left:293px">Our Brands</a>
    <a class="nav-link" style="left:572px">About</a>
    <a class="nav-link" style="left:674px">Contact</a>
    <a class="nav-link" style="left:798px">Blog</a>
    <div class="nav-rule" style="left:54px;width:342px"></div>
    <div class="nav-rule" style="left:553px;width:341px"></div>
    <div class="search-field">Search</div>
    <div class="brand-badge"><span>Verdant<br>Twin</span></div>
  </header>

  <h1 class="page-title">Water Pipes</h1>

  <main>
    <article class="product" style="left:112px;top:212px"><div class="product-photo photo-clear-trio" role="img" aria-label="Three clear glass water pipes with coloured bases"></div><p class="product-name">Crystal Water Pipe</p><p class="product-price">$29.99</p><button class="add-to-cart">ADD TO CART</button></article>
    <article class="product" style="left:367px;top:212px"><div class="product-photo photo-acrylic" role="img" aria-label="Blue, green and red acrylic water pipes"></div><p class="product-name">Crystal Water Pipe</p><p class="product-price">$29.99</p><button class="add-to-cart">ADD TO CART</button></article>
    <article class="product" style="left:618px;top:212px"><div class="product-photo photo-amber-tall" role="img" aria-label="Tall glass water pipe with amber accents"></div><p class="product-name">Crystal Water Pipe</p><p class="product-price">$29.99</p><button class="add-to-cart">ADD TO CART</button></article>

    <article class="product" style="left:112px;top:523px"><div class="product-photo photo-clear-beaker" role="img" aria-label="Clear glass beaker water pipe with percolator"></div><p class="product-name">Crystal Water Pipe</p><p class="product-price">$29.99</p><button class="add-to-cart">ADD TO CART</button></article>
    <article class="product" style="left:367px;top:523px"><div class="product-photo photo-bubbler-row" role="img" aria-label="Row of small colourful glass bubblers"></div><p class="product-name">Crystal Water Pipe</p><p class="product-price">$29.99</p><button class="add-to-cart">ADD TO CART</button></article>
    <article class="product" style="left:618px;top:523px"><div class="product-photo photo-navy-amber" role="img" aria-label="Beaker water pipe with blue and amber glass"></div><p class="product-name">Crystal Water Pipe</p><p class="product-price">$29.99</p><button class="add-to-cart">ADD TO CART</button></article>

    <article class="product" style="left:112px;top:830px"><div class="product-photo photo-striped" role="img" aria-label="Curved glass bubbler with red and yellow stripes"></div><p class="product-name">Crystal Water Pipe</p><p class="product-price">$29.99</p><button class="add-to-cart">ADD TO CART</button></article>
    <article class="product" style="left:367px;top:830px"><div class="product-photo photo-assorted" role="img" aria-label="Group of assorted clear glass water pipes"></div><p class="product-name">Crystal Water Pipe</p><p class="product-price">$29.99</p><button class="add-to-cart">ADD TO CART</button></article>
    <article class="product" style="left:618px;top:830px"><div class="product-photo photo-slim-green" role="img" aria-label="Slim straight glass water pipe with green accents"></div><p class="product-name">Crystal Water Pipe</p><p class="product-price">$29.99</p><button class="add-to-cart">ADD TO CART</button></article>
  </main>

  <footer class="site-footer"></footer>
  <a class="social" style="left:397px;background:var(--social-1)">Pals</a>
  <a class="social" style="left:442px;background:var(--social-2)">Hum</a>
  <a class="social" style="left:486px;background:var(--social-3)">Lenso</a>
  <a class="social" style="left:532px;background:var(--social-4)">Vidora</a>
</body>
</html>
```